Liquor Label / Aguardiente

Label design for liquor bottle. Designers may submit multiple submissions.

Product Description:
Name: Viento de Plata™
Alcohol Category: Aguardiente (which in Spanish most closely translates to “burning water”) – aguardiente is derived from
cane sugar and is a general term for a type of alcoholic spirit in many Central and South America countries.
Taste: A smooth liquor with a comfortable yet spicy finish
Smell: Subtle aroma of spicy jalapeños
Liquid Color: Clear
Bottle Color: Clear
See link for reference - http://www.kelvostamp.com/sites/default/files/styles/uc_product_full/public/Pemrow_0.jpg?itok=9QmT2xLp
Closure: Bar top / cork
Bottle Shape/Size: height = 8.67in; diameter of base = 3.70in; diameter of neck = 0.85in

Label may consist of two separate parts (i.e. front and back, front and vertical side), or one continuous label.

Designer has complete freedom with color, font etc. unless otherwise stated below. The label MUST
contain (but is not limited only to) the following text exactly as written in quotes below:
- “Viento de Plata”
- “Aguardiente”
- “Cane Neutral Spirit with Natural Flavors”
- “35% Alc./Vol.”
- “750 ml”
- “Bottled by WP Spirits, LLC” and “Cedarbrook, TN” - “Government Warning: (1) According to the Surgeon General, women should not drink alcoholic beverages during
pregnancy because of the risk of birth defects. (2) Consumption of alcoholic beverages impairs your ability to
drive a car or operate machinery, and may cause health problems.” (text in previous quotes must be in all
capitalized letters, text must be 2 MM in height and quote must be separated 2MM by all other text)
- Must be dedicated empty space for bar code (approximately 0.75in. height x 1.25in. length)

Target Market(s)

Label should have mass market appeal.
Age: 21 – 28 years old (primary target market is 21+ year old college students and recent graduates)
Target Market Gender: Both male and female, with emphasis on male
Consumption Focus: Spirit will be consumed typically as a shot, primarily at bars and secondarily off premise (label design will be critical for making our product highly visible behind a bar)
Marketing Theme: South American elements. The official Viento de Plata mascot is a llama and the incorporation and use of a llama somewhere (however large or small) on the bottle is encourage but by no means required.

Industry/Entity Type

Health

Requirements
Should not have
• Elements that may lead a potential consumer to believe the beverage is a craft liquor or an artisan brand. Please do not include images of peppers.

```html
<!DOCTYPE html>
<html lang="en">
<head>
<meta charset="utf-8">
<title>Viento de Plata™ Aguardiente – Label</title>
<link rel="stylesheet" href="https://fonts.googleapis.com/css2?family=Oswald:wght@400;600&family=Playball&family=Raleway:wght@300&family=Open+Sans:wght@400;700&display=swap">
<style>
  :root {
    --backdrop: #d9d9d9;
    --label-brown: #4a3320;
    --cream: #e3d0a0;
    --flame-deep: #7a3c22;
    --flame-light: #a4573a;
  }
  * { margin: 0; padding: 0; box-sizing: border-box; }
  html, body { width: 1200px; height: 910px; overflow: hidden; }
  body {
    background: var(--backdrop);
    position: relative;
    font-family: "Open Sans", sans-serif;
  }

  /* Front label */
  .front-label {
    position: absolute;
    left: 230px; top: 86px;
    width: 584px; height: 737px;
    background: var(--label-brown);
    overflow: hidden;
    color: var(--cream);
  }
  .flame-band {
    position: absolute;
    top: 0; bottom: 0;
    width: 78px;
    opacity: .75;
  }
  .flame-band--left {
    left: 0;
    background: linear-gradient(90deg, var(--flame-light) 0%, var(--flame-deep) 45%, rgba(74,51,32,0) 100%);
  }
  .flame-band--right {
    right: 0;
    background: linear-gradient(270deg, var(--flame-light) 0%, var(--flame-deep) 45%, rgba(74,51,32,0) 100%);
  }
  .mascot {
    position: absolute;
    background: linear-gradient(180deg, #ece0bd, #cdb98a);
  }
  .front-label .mascot { left: 238px; top: 0; width: 108px; height: 143px; }

  .brand-word {
    position: absolute;
    top: 94px;
    font-family: "Oswald", sans-serif;
    font-weight: 400;
    font-size: 34px;
    letter-spacing: .5px;
    line-height: 1;
    white-space: nowrap;
  }
  .brand-word--left { right: 356px; }
  .brand-word--right { left: 356px; }
  .brand-word sup { font-size: 14px; vertical-align: 16px; }

  .category {
    position: absolute;
    left: -20px; right: -20px;
    top: 160px;
    text-align: center;
    font-family: "Playball", cursive;
    font-weight: 400;
    font-size: 118px;
    line-height: 1.3;
    white-space: nowrap;
  }
  .descriptor {
    position: absolute;
    left: 0; right: 0; top: 344px;
    text-align: center;
    font-family: "Raleway", sans-serif;
    font-weight: 300;
    font-size: 19px;
    letter-spacing: .3px;
  }
  .rule {
    position: absolute;
    left: 70px; width: 446px; height: 2px;
    background: var(--cream);
  }
  .rule--top { top: 408px; }
  .rule--bottom { top: 476px; }
  .specs {
    position: absolute;
    left: 70px; width: 446px; top: 410px; height: 66px;
    display: flex; align-items: center;
    font-family: "Raleway", sans-serif;
    font-weight: 300;
    font-size: 25px;
  }
  .specs__volume { width: 159px; text-align: center; }
  .specs__divider { width: 2px; height: 36px; background: var(--cream); }
  .specs__abv { flex: 1; text-align: center; }
  .bottler {
    position: absolute;
    left: 0; right: 0; top: 490px;
    text-align: center;
    font-family: "Oswald", sans-serif;
    font-weight: 600;
    font-size: 12.5px;
    letter-spacing: .3px;
  }
  .warning {
    position: absolute;
    left: 70px; top: 558px; width: 276px;
    font-size: 12.3px;
    line-height: 20.5px;
  }
  .warning strong { font-weight: 700; }
  .warning-divider {
    position: absolute;
    left: 388px; top: 559px;
    width: 2px; height: 132px;
    background: var(--cream);
  }
  .barcode-space {
    position: absolute;
    left: 439px; top: 559px;
    width: 85px; height: 133px;
    background: var(--cream);
  }

  /* Neck strip */
  .neck-strip {
    position: absolute;
    left: 900px; top: 86px;
    width: 74px; height: 737px;
    background: var(--label-brown);
    color: var(--cream);
  }
  .neck-strip__name {
    position: absolute;
    left: 0; width: 74px;
    writing-mode: vertical-rl;
    transform: rotate(180deg);
    display: flex; align-items: center; justify-content: center;
    font-family: "Oswald", sans-serif;
    font-size: 27px;
    white-space: nowrap;
  }
  .neck-strip__name sup { font-size: 12px; }
  .neck-strip__name--top { top: 20px; height: 240px; }
  .neck-strip__name--bottom { top: 470px; height: 250px; }
  .neck-strip .mascot { left: 4px; top: 323px; width: 66px; height: 98px; }
</style>
</head>
<body>

<section class="front-label">
  <div class="flame-band flame-band--left" role="img" aria-label="Flame ornament along the left edge"></div>
  <div class="flame-band flame-band--right" role="img" aria-label="Flame ornament along the right edge"></div>

  <div class="mascot" role="img" aria-label="Engraved llama mascot portrait with sunburst"></div>
  <div class="brand-word brand-word--left">VIENTO DE</div>
  <div class="brand-word brand-word--right">PLATA<sup>TM</sup></div>

  <h1 class="category">Aguardiente</h1>
  <p class="descriptor">CANE NEUTRAL SPIRIT WITH NATURAL FLAVORS</p>

  <div class="rule rule--top"></div>
  <div class="specs">
    <span class="specs__volume">750 ML</span>
    <span class="specs__divider"></span>
    <span class="specs__abv">35% ALC./VOL.</span>
  </div>
  <div class="rule rule--bottom"></div>

  <p class="bottler">BOTTLED BY WP SPIRITS, LLC &amp; CEDARBROOK, TN</p>

  <p class="warning"><strong>Government Warning:</strong><br>
    According to the Surgeon General, women should not drink alcoholic beverages during pregnancy because of the risk of birth defects. Consumption of alcoholic beverages impairs your ability to drive a car or operate machinery, and may cause health problems.</p>
  <div class="warning-divider"></div>
  <div class="barcode-space" aria-label="Reserved barcode space"></div>
</section>

<aside class="neck-strip">
  <div class="neck-strip__name neck-strip__name--top">VIENTO DE PLATA<sup>TM</sup></div>
  <div class="mascot" role="img" aria-label="Llama mascot portrait"></div>
  <div class="neck-strip__name neck-strip__name--bottom">VIENTO DE PLATA<sup>TM</sup></div>
</aside>

</body>
</html>
```